Senior sex novelty store providing a private method for acquiring the products and knowledge

Our business supplies novelty sex products and services, specializing in the 50+ demographic. Products include sex products for individuals and couples. Services include webinars and teleseminars that address various sex and relationship issues. We are dedicated to providing discreet delivery of products and knowledge to people over 50 entering a new phase of life, facing new challenges. Our entire process from site through shipping is kept private to allow our customers the freedom to shop and learn in the privacy of their own home.

Target Market(s)

Seniors over 50 years old

Industry/Entity Type

Store

Number of Pages Required

1 page

Font styles to use
Serif

Requirements
Must have
• place for business description with a private look
Should not have
• anything sleazy

```html
<!DOCTYPE html>
<html lang="en">
<head>
<meta charset="utf-8">
<title>Private Store – Home</title>
<link rel="stylesheet" href="https://fonts.googleapis.com/css2?family=Josefin+Sans:wght@300;400;600&family=Arimo:wght@400;700&family=Nunito:wght@700&family=Oswald:wght@600&display=swap">
<style>
  :root {
    --rust: #bd4608;
    --rust-deep: #b53d12;
    --ember: #f25a22;
    --panel: rgba(58, 52, 49, 0.78);
    --panel-soft: rgba(62, 56, 52, 0.5);
    --ink: #111111;
    --cream: #f3ece8;
    --stone: #b5b0ae;
    --muted: #a8a4a2;
    --white: #ffffff;
  }
  * { box-sizing: border-box; margin: 0; padding: 0; }
  html, body { width: 1200px; height: 2278px; overflow: hidden; background: var(--white); }
  body { position: relative; font-family: "Josefin Sans", sans-serif; }

  .hero {
    position: absolute; left: 0; top: 0; width: 1200px; height: 892px;
    background:
      radial-gradient(ellipse at 62% 40%, rgba(196, 120, 90, 0.55), transparent 45%),
      linear-gradient(160deg, #2e2823 0%, #6d5f52 30%, #a99683 55%, #7c6c5d 75%, #cbb8a2 100%);
  }

  .main-nav {
    position: absolute; left: 123px; top: 46px; width: 959px; height: 53px;
    background: var(--panel);
  }
  .nav-links {
    position: absolute; left: 38px; top: 0; height: 53px; width: 600px;
    display: flex; align-items: center; justify-content: space-between;
  }
  .nav-links a {
    color: var(--cream); text-decoration: none; font-weight: 300; white-space: nowrap;
    font-size: 17px; letter-spacing: 1px; text-transform: uppercase; padding-top: 3px;
  }
  .search {
    position: absolute; right: 19px; top: 9px; width: 266px; height: 36px;
    background: var(--ember); border-radius: 18px; display: flex; align-items: center;
    padding: 0 16px 0 20px; font-family: "Arimo", sans-serif; font-size: 15px; color: #3a1a0a;
  }
  .search span { flex: 1; }

  .cart-box {
    position: absolute; left: 123px; top: 120px; width: 175px; height: 150px;
    background: var(--panel); color: var(--ember); text-align: right; padding: 18px 16px 0 0;
    font-size: 19px; line-height: 26px; font-weight: 300; text-transform: uppercase;
  }
  .cart-box svg { position: absolute; left: 12px; top: 14px; }
  .cart-box .total { font-family: "Arimo", sans-serif; font-weight: 700; text-transform: none; font-size: 17px; }

  .welcome {
    position: absolute; left: 32px; top: 342px; width: 610px; height: 465px;
    background: var(--panel-soft); padding: 18px 6px 0 32px; color: var(--cream);
  }
  .welcome-title {
    display: flex; align-items: center; justify-content: center; gap: 22px;
    font-weight: 300; font-size: 36px; letter-spacing: 4px; margin-bottom: 22px; padding-right: 70px;
    text-transform: uppercase;
  }
  .welcome p {
    font-size: 19px; line-height: 21px; text-transform: uppercase; letter-spacing: 0.4px;
    text-align: left; margin-bottom: 14px;
  }

  .shop-now {
    position: absolute; left: 703px; top: 699px; width: 379px; height: 87px;
    background: #4a4541; color: var(--ember); font-family: "Oswald", sans-serif;
    font-weight: 600; font-size: 60px; display: flex; align-items: center; justify-content: center;
    text-decoration: none;
  }

  .card {
    position: absolute; top: 993px; width: 450px; height: 450px; border: 3px solid var(--ink);
    background: var(--stone);
  }
  .card-title {
    height: 80px; background: var(--rust); color: var(--cream); font-weight: 300;
    font-size: 56px; letter-spacing: 5px; padding: 14px 0 0 46px;
  }
  .card-text {
    padding: 60px 52px 0 52px; font-family: "Arimo", sans-serif; font-size: 16px;
    line-height: 19px; color: var(--rust-deep); letter-spacing: 0.8px; text-align: left;
  }
  .card-media {
    height: 364px;
    background: linear-gradient(135deg, #c0160f 0%, #8a1610 45%, #3a1412 75%, #d6392a 100%);
  }
  .card-one { left: 123px; }
  .card-two { left: 627px; }

  .how-it-works {
    position: absolute; left: 0; top: 1509px; width: 1200px; height: 536px; background: var(--rust);
    color: var(--cream);
  }
  .how-title {
    position: absolute; top: 56px; width: 100%; text-align: center; font-weight: 300;
    font-size: 68px; letter-spacing: 7px;
  }
  .step-label {
    position: absolute; font-family: "Nunito", sans-serif; font-weight: 700; font-size: 32px;
    letter-spacing: 0.5px; transform: translateX(-50%); white-space: nowrap; color: #f0ddd3;
  }
  .step-icon { position: absolute; }

  .site-footer {
    position: absolute; top: 2170px; width: 100%; text-align: center;
    font-family: "Nunito", sans-serif; font-weight: 700; color: var(--muted); font-size: 31px; line-height: 42px;
  }
</style>
</head>
<body>

<div class="hero" role="img" aria-label="Photo of a woman relaxing on sunlit sand dunes in an orange swimsuit"></div>

<nav class="main-nav">
  <div class="nav-links">
    <a href="#">Home</a>
    <a href="#">My Account</a>
    <a href="#">Services</a>
    <a href="#">Products</a>
    <a href="#">About Us</a>
  </div>
  <div class="search">
    <span>Type here to search...</span>
    <svg width="20" height="20" viewBox="0 0 20 20" aria-hidden="true">
      <circle cx="8" cy="8" r="6" fill="none" stroke="#1a0c05" stroke-width="2.6"/>
      <line x1="12.5" y1="12.5" x2="18" y2="18" stroke="#1a0c05" stroke-width="3"/>
    </svg>
  </div>
</nav>

<aside class="cart-box">
  <svg width="32" height="28" viewBox="0 0 32 28" aria-hidden="true">
    <path d="M1 3h5l4 15h16l4-11H8" fill="none" stroke="#f3ece8" stroke-width="2"/>
    <circle cx="12" cy="24" r="2.2" fill="#f3ece8"/>
    <circle cx="24" cy="24" r="2.2" fill="#f3ece8"/>
  </svg>
  <div>Product</div>
  <div class="total">Total: 123$</div>
  <div>Name Name</div>
  <div>Sign Out</div>
</aside>

<section class="welcome">
  <h1 class="welcome-title">
    <svg width="40" height="52" viewBox="0 0 40 52" aria-hidden="true">
      <path d="M9 22V14a11 11 0 0 1 22 0v8" fill="none" stroke="#f3ece8" stroke-width="5"/>
      <rect x="2" y="22" width="36" height="29" rx="3" fill="#f3ece8"/>
      <rect x="18" y="30" width="4" height="12" fill="#5a514c"/>
    </svg>
    <span>Welcome !</span>
  </h1>
  <p>Our company providing a private method for acquiring the products and knowledge.</p>
  <p>Lorem ipsum dolor sit amet, consectetur adipisicing elit, sed do eiusmod tempor incididunt ut labore et dolore magna aliqua. Ut enim ad minim veniam, quis nostrud exercitation ullamco laboris nisi ut aliquip ex ea commodo consequat. Duis aute irure dolor in reprehenderit in voluptate velit esse cillum dolore eu fugiat nulla pariatur. Excepteur sint occaecat cupidatat non proident, sunt in culpa qui officia deserunt mollit anim id est laborum. Sed ut perspiciatis unde omnis iste natus error sit voluptatem accusantium doloremque laudantium, totam rem aperiam, eaque ipsa quae ab illo inventore veritatis et quasi architecto beatae vitae.</p>
</section>

<a class="shop-now" href="#">SHOP NOW!</a>

<article class="card card-one">
  <h2 class="card-title">TITLE</h2>
  <p class="card-text">Lorem ipsum dolor sit amet, consectetur adipisicing elit, sed do eiusmod tempor incididunt ut labore et dolore magna aliqua. Ut enim ad minim veniam, quis nostrud exercitation ullamco laboris nisi ut aliquip ex ea commodo consequat. Duis aute irure dolor in reprehenderit in voluptate velit esse cillum dolore eu fugiat nulla pariatur. Excepteur sint occaecat cupidatat non proident, sunt in culpa qui officia deserunt m</p>
</article>

<article class="card card-two">
  <h2 class="card-title">TITLE</h2>
  <div class="card-media" role="img" aria-label="Photo of a red-haired woman in a black top against a red background"></div>
</article>

<section class="how-it-works">
  <h2 class="how-title">HOW IT WORKS</h2>

  <svg class="step-icon" style="left:104px;top:186px" width="200" height="190" viewBox="0 0 200 190" aria-hidden="true">
    <g fill="none" stroke="#f3ece8" stroke-width="9" stroke-linejoin="round" stroke-linecap="round">
      <path d="M6 8h28l36 126h100"/>
      <path d="M44 46h148l-22 74H64"/>
      <line x1="84" y1="46" x2="90" y2="120"/>
      <line x1="118" y1="46" x2="118" y2="120"/>
      <line x1="152" y1="46" x2="146" y2="120"/>
      <line x1="52" y1="82" x2="181" y2="82"/>
    </g>
    <circle cx="86" cy="164" r="13" fill="none" stroke="#f3ece8" stroke-width="8"/>
    <circle cx="156" cy="164" r="13" fill="none" stroke="#f3ece8" stroke-width="8"/>
  </svg>

  <div class="step-label" style="left:580px;top:230px;font-size:30px">We deliver to you</div>
  <svg class="step-icon" style="left:448px;top:294px" width="290" height="30" viewBox="0 0 290 30" aria-hidden="true">
    <line x1="0" y1="15" x2="240" y2="15" stroke="#c9c4c1" stroke-width="5"/>
    <polygon points="228,3 290,15 228,27" fill="#c9c4c1"/>
  </svg>

  <svg class="step-icon" style="left:862px;top:208px" width="212" height="178" viewBox="0 0 212 178" aria-hidden="true">
    <g fill="none" stroke="#f3ece8" stroke-width="8" stroke-linejoin="round">
      <polygon points="106,40 176,62 106,86 36,62" fill="#f3ece8"/>
      <polygon points="36,62 6,32 72,8 106,40"/>
      <polygon points="176,62 206,32 140,8 106,40"/>
      <polygon points="36,62 8,94 78,120 106,86"/>
      <polygon points="176,62 204,94 134,120 106,86"/>
      <polyline points="40,108 40,142 106,172 172,142 172,108"/>
      <line x1="106" y1="110" x2="106" y2="172"/>
    </g>
  </svg>

  <div class="step-label" style="left:231px;top:410px">Choose a product</div>
  <div class="step-label" style="left:955px;top:410px">Acquiring in a private way</div>
</section>

<footer class="site-footer">
  <div>All rights reserved</div>
  <div>0000</div>
</footer>

</body>
</html>
```